Brightmoor Capital
"The Business and Corporate Finance Specialists, Mortgages and Remortgages"
Professional
Dorian Kellaway
Director
14 Quillfield Parade
Harrow
London
HA7 2QX
Dorian@brightmoorcapital.example
www.brightmoorcapital.example
Letterhead and compliment slips require the following regulatory text:
"Registered in England and Wales number: 08213947
Brightmoor Capital Ltd is authorised and regulated by the Monetary Oversight Council for regulated mortgage contracts and non-investment insurance activities."
Be creative - open to suggestions

```html
<!DOCTYPE html>
<html lang="en">
<head>
<meta charset="utf-8">
<title>Brightmoor Capital – Business Cards</title>
<link href="https://fonts.googleapis.com/css2?family=Arimo:wght@400;700&display=swap" rel="stylesheet">
<style>
  :root {
    --backdrop: #e9e4dc;
    --card: #0b0b0b;
    --card-edge: #1c1c1c;
    --brand-orange: #f28c1c;
    --brand-gold: #f5c000;
    --brand-green: #8cc63f;
    --text-light: #f2f2f2;
    --text-muted: #b9b9b9;
  }
  * { box-sizing: border-box; margin: 0; padding: 0; }
  html, body { width: 1200px; height: 646px; overflow: hidden; }
  body {
    background: var(--backdrop);
    font-family: "Arimo", Arial, sans-serif;
    display: flex;
    align-items: center;
    justify-content: center;
    gap: 60px;
  }
  .card {
    position: relative;
    width: 520px;
    height: 300px;
    background: var(--card);
    border: 1px solid var(--card-edge);
    box-shadow: 0 10px 28px rgba(0,0,0,.25);
    overflow: hidden;
    color: var(--text-light);
  }
  .brand { display: flex; align-items: center; gap: 12px; }
  .brand-dot {
    width: 30px; height: 30px; border-radius: 50%;
    background: var(--brand-orange);
  }
  .brand-name {
    font-size: 30px; font-weight: 700; color: var(--brand-orange);
    letter-spacing: -0.5px;
  }
  .tagline {
    font-size: 12px; line-height: 1.3; color: var(--text-light);
    margin-top: 6px;
  }
  .web { font-size: 11px; color: var(--text-muted); margin-top: 8px; }

  /* Front */
  .card-front .brand-block {
    position: absolute; left: 150px; top: 104px;
  }
  .card-front .brand-block .tagline { margin-left: 42px; }
  .card-front .brand-block .web { margin-left: 42px; }

  /* Back */
  .card-back .accent-bar {
    position: absolute; left: 0; top: 150px; width: 10px; height: 150px;
    background: linear-gradient(to bottom, var(--brand-gold), var(--brand-orange));
  }
  .card-back .brand-block { position: absolute; left: 150px; top: 36px; }
  .card-back .brand-block .tagline { margin-left: 42px; }
  .person { position: absolute; right: 34px; top: 150px; text-align: right; }
  .person-name { font-size: 16px; font-weight: 700; color: var(--brand-orange); }
  .person-role { font-size: 11px; color: var(--brand-orange); margin-top: 2px; }
  .address {
    position: absolute; left: 34px; top: 150px;
    font-size: 11px; line-height: 1.4; color: var(--text-light); font-style: normal;
  }
  .contacts { position: absolute; left: 34px; top: 192px; list-style: none; }
  .contacts li {
    display: flex; align-items: center; gap: 8px;
    font-size: 11px; line-height: 1; color: var(--text-light); margin-bottom: 6px;
  }
  .contacts svg { width: 12px; height: 12px; flex: none; }
</style>
</head>
<body>
  <section class="card card-front">
    <div class="brand-block">
      <div class="brand">
        <span class="brand-dot"></span>
        <span class="brand-name">Brightmoor Capital</span>
      </div>
      <p class="tagline">Business and Corporate Finance Specialists<br>Mortgages and Remortgages</p>
      <p class="web">www.brightmoorcapital.example</p>
    </div>
  </section>

  <section class="card card-back">
    <div class="accent-bar"></div>
    <div class="brand-block">
      <div class="brand">
        <span class="brand-dot"></span>
        <span class="brand-name">Brightmoor Capital</span>
      </div>
      <p class="tagline">Business and Corporate Finance Specialists<br>Mortgages and Remortgages</p>
    </div>

    <address class="address">14 Quillfield Parade<br>Harrow, London HA7 2QX</address>

    <ul class="contacts">
      <li>
        <svg viewBox="0 0 12 12"><path d="M2 1h2.5l1 3-1.5 1a6 6 0 0 0 3 3l1-1.5 3 1V11a1 1 0 0 1-1 1A10 10 0 0 1 1 2a1 1 0 0 1 1-1z" fill="var(--brand-orange)"/></svg>
        +44 (0) 208 555 0142
      </li>
      <li>
        <svg viewBox="0 0 12 12"><rect x="3" y="0.5" width="6" height="11" rx="1" fill="var(--brand-orange)"/><rect x="4" y="2" width="4" height="7" fill="var(--card)"/></svg>
        +44 (0) 7700 900 318
      </li>
      <li>
        <svg viewBox="0 0 12 12"><rect x="1" y="4" width="10" height="6" fill="var(--brand-orange)"/><rect x="3" y="1" width="6" height="3" fill="var(--brand-orange)"/></svg>
        +44 (0) 208 555 0197
      </li>
      <li>
        <svg viewBox="0 0 12 12"><rect x="0.5" y="2" width="11" height="8" fill="var(--brand-orange)"/><path d="M1 2.5l5 4 5-4" stroke="var(--card)" fill="none"/></svg>
        Dorian@brightmoorcapital.example
      </li>
      <li>
        <svg viewBox="0 0 12 12"><circle cx="6" cy="6" r="5.5" fill="var(--brand-orange)"/><path d="M0.5 6h11M6 .5c-3 3-3 8 0 11M6 .5c3 3 3 8 0 11" stroke="var(--card)" fill="none" stroke-width=".8"/></svg>
        www.brightmoorcapital.example
      </li>
    </ul>

    <div class="person">
      <p class="person-name">Dorian Kellaway</p>
      <p class="person-role">Director</p>
    </div>
  </section>
</body>
</html>
```